Cyber Security Consultancy needs website design.

We need a website design for a cyber security startup in Dubai.

Coding

Coded - Design and coding required

Number of Pages Required

1 page

Colors
0054AA
0677BA
7BADD7
CADEEF
E8F1F8

```html
<!DOCTYPE html>
<html lang="en">
<head>
<meta charset="utf-8">
<title>Vantage Keep — Cyber Security Consultancy</title>
<link href="https://fonts.googleapis.com/css2?family=Montserrat:wght@300;400;700;800&family=Roboto:wght@300;400;500;700&family=Open+Sans:wght@700&display=swap" rel="stylesheet">
<style>
:root{
  --brand-deep:#0054AA;
  --brand:#0677BA;
  --brand-soft:#7BADD7;
  --brand-pale:#CADEEF;
  --brand-mist:#E8F1F8;
  --ink:#000;
  --night:#03060d;
  --text-dark:#2a2a2a;
  --text-muted:#8a8a8a;
  --white:#fff;
}
*{box-sizing:border-box;margin:0;padding:0}
html,body{width:1200px;height:2584px;overflow:hidden}
body{font-family:"Roboto",Arial,sans-serif;background:var(--white);color:var(--text-dark);position:relative}
a{text-decoration:none;color:inherit}

/* ---------- Hero ---------- */
.hero{position:absolute;left:0;top:0;width:1200px;height:682px;background:var(--ink);overflow:hidden}
.hero-visual{position:absolute;left:560px;top:0;width:640px;height:682px;
  background:radial-gradient(circle at 280px 330px,#1f8fe0 0,#0b4d9a 22%,#06244f 45%,#020812 72%);}
.brand{position:absolute;display:flex;align-items:center;gap:12px;font-family:"Open Sans",sans-serif;font-weight:700;color:var(--white)}
.brand-mark{width:26px;height:26px;border-radius:50%;background:var(--brand)}
.hero .brand{left:111px;top:44px;font-size:25px}
.contact-bar{position:absolute;right:112px;top:32px;display:flex;gap:24px;font-size:16px;font-weight:500}
.contact-bar span{display:flex;align-items:center;gap:8px}
.contact-bar .phone{color:var(--brand-soft)}
.contact-bar .mail{color:var(--white)}
.nav{position:absolute;right:112px;top:76px;display:flex;align-items:center;gap:36px;font-size:14px;font-weight:500;color:var(--white)}
.nav .active{color:var(--brand-soft)}
.nav .quote{background:var(--brand-deep);padding:9px 19px;font-weight:700}
.hero-copy{position:absolute;left:114px;top:222px;width:420px}
.hero-kicker{font-family:"Montserrat",sans-serif;font-weight:300;font-size:28px;color:var(--white)}
.hero-title{font-family:"Montserrat",sans-serif;font-weight:800;font-size:40px;line-height:57px;color:var(--brand);margin-top:4px}
.hero-text{font-family:"Montserrat",sans-serif;font-size:14px;line-height:23px;color:var(--white);margin-top:14px}
.btn-outline{display:inline-block;margin-top:26px;width:142px;height:40px;line-height:36px;text-align:center;border:2px solid var(--white);background:var(--brand);color:var(--white);font-size:14px}
.dots{position:absolute;left:555px;top:627px;display:flex;gap:10px}
.dots i{width:14px;height:14px;border:2px solid var(--white);border-radius:50%}
.dots i.on{background:var(--brand);border-color:var(--brand-soft)}

/* ---------- Services ---------- */
.services{position:absolute;left:0;top:682px;width:1200px;height:777px;background:var(--white)}
.section-title{font-family:"Roboto",sans-serif;font-weight:700;font-size:38px;color:var(--text-dark)}
.section-title em{font-style:normal;color:var(--brand)}
.services .section-title{position:absolute;top:60px;width:100%;text-align:center}
.services .rule{position:absolute;left:563px;top:113px;width:72px;height:4px;background:var(--brand)}
.services .lede{position:absolute;top:130px;width:100%;text-align:center;font-size:16px;color:#555}
.cards{position:absolute;left:111px;top:177px;display:flex;gap:44px}
.card{width:297px;text-align:center}
.card-media{height:283px;border-radius:8px}
.media-infra{background:linear-gradient(160deg,#0e3a52,#06141f 70%)}
.media-app{background:linear-gradient(160deg,#6b2fa8,#e46a4b 45%,#1d2c70)}
.media-red{background:linear-gradient(180deg,#1b3f7a,#3a0a12 60%,#0a0a0c)}
.card h3{font-weight:400;font-size:20px;line-height:25px;margin-top:43px;height:50px;color:var(--text-dark)}
.card.featured h3{color:var(--brand)}
.card p{font-size:13px;line-height:22px;color:var(--text-muted);margin-top:8px;padding:0 8px}
.read-more{display:inline-flex;align-items:center;gap:10px;margin-top:12px;font-size:12px;text-decoration:underline;color:var(--text-dark)}
.read-more b{width:22px;height:22px;border-radius:50%;background:#111;color:var(--white);font-size:12px;line-height:22px;text-decoration:none}
.featured .read-more{color:var(--brand)}
.featured .read-more b{background:var(--brand)}

/* ---------- About ---------- */
.about{position:absolute;left:0;top:1459px;width:1200px;height:594px;background:linear-gradient(180deg,#040c1d,#0b2a55 60%,#0c3a5e);overflow:hidden}
.about-visual{position:absolute;left:573px;top:90px;width:627px;height:504px;background:radial-gradient(ellipse at 60% 40%,#0a6dc2 0,#0a3d78 40%,rgba(6,30,70,0) 75%)}
.about-copy{position:absolute;left:111px;top:105px;width:480px;color:var(--white)}
.about .section-title{color:var(--white)}
.about .rule{width:64px;height:4px;background:var(--white);margin-top:8px}
.about h4{font-size:16px;line-height:23px;font-weight:700;margin-top:12px}
.about p{font-size:13px;line-height:22px;margin-top:8px}
.about p+p{margin-top:20px}
.btn-solid{display:inline-block;margin-top:24px;background:var(--brand);color:var(--white);font-weight:700;font-size:13px;padding:10px 18px}

/* ---------- Footer ---------- */
.footer{position:absolute;left:0;top:2053px;width:1200px;height:531px;background:var(--ink);color:var(--white)}
.footer .brand{left:111px;top:58px;font-size:46px;gap:18px}
.footer .brand-mark{width:44px;height:44px}
.social{position:absolute;right:124px;top:80px;display:flex;gap:14px}
.social i{width:16px;height:16px;border-radius:50%;background:var(--white)}
.social i:first-child{background:var(--brand-soft)}
.cols{position:absolute;left:111px;top:176px;width:978px;height:290px;border-bottom:1px solid #333;display:flex}
.col{position:relative;border-left:1px solid #333;padding:70px 0 0 26px}
.col::before{content:"";position:absolute;left:-3px;top:36px;width:5px;height:76px;border-radius:3px;background:#555}
.col:nth-child(1){width:385px}
.col:nth-child(2){width:305px;padding-left:26px}
.col:nth-child(3){flex:1}
.col h5{color:var(--brand);font-size:16px;font-weight:700;margin-bottom:16px}
.col li{list-style:none;font-size:13px;line-height:27px;display:flex;align-items:center;gap:6px}
.col li i{width:12px;height:12px;border:2px solid var(--brand);border-radius:50%}
.reach p{font-size:13px;line-height:27px;display:flex;gap:6px;align-items:flex-start}
.reach p+p{margin-top:28px}
.reach svg{margin-top:6px;flex:none}
.subscribe p{font-size:13px;line-height:27px;width:240px}
.subscribe-form{display:flex;margin-top:16px;width:261px;height:50px}
.subscribe-form span{flex:1;border:1px solid var(--white);border-right:0;font-size:12px;color:#aaa;padding:16px 24px}
.subscribe-form b{width:66px;background:var(--brand);display:flex;align-items:center;justify-content:center}
.copyright{position:absolute;top:494px;width:100%;text-align:center;font-size:11px;color:#bbb}
</style>
</head>
<body>

<header class="hero">
  <div class="hero-visual" role="img" aria-label="Open hand holding a glowing blue padlock surrounded by security icons"></div>
  <div class="brand"><span class="brand-mark"></span>VANTAGE KEEP</div>
  <div class="contact-bar">
    <span class="phone"><svg width="22" height="22" viewBox="0 0 24 24"><path fill="#0677BA" d="M6.6 10.8a15 15 0 0 0 6.6 6.6l2.2-2.2c.3-.3.7-.4 1-.2 1.1.4 2.3.6 3.6.6.6 0 1 .4 1 1V20c0 .6-.4 1-1 1A17 17 0 0 1 3 4c0-.6.4-1 1-1h3.5c.6 0 1 .4 1 1 0 1.3.2 2.5.6 3.6.1.3 0 .7-.2 1z"/></svg>+1 555 014 2200</span>
    <span class="mail"><svg width="26" height="20" viewBox="0 0 26 20"><rect x="1" y="1" width="24" height="18" fill="#fff"/><path d="M1 1l12 10L25 1" stroke="#000" stroke-width="2" fill="none"/></svg>hello@vantagekeep.example</span>
  </div>
  <nav class="nav">
    <a class="active">HOME</a><a>ABOUT US</a><a>SERVICES</a><a>CONTACT</a><a class="quote">GET A QUOTE</a>
  </nav>
  <div class="hero-copy">
    <div class="hero-kicker">Vantage Keep</div>
    <h1 class="hero-title">Cyber Security<br>Consultancy</h1>
    <p class="hero-text">Lorem Ipsum is simply dummy text of the printing and typesetting industry. Lorem Ipsum has been the industry's standard dummy text ever since the 1500s,</p>
    <a class="btn-outline">Get started</a>
  </div>
  <div class="dots"><i class="on"></i><i></i><i></i><i></i></div>
</header>

<section class="services">
  <h2 class="section-title">Our <em>Services</em></h2>
  <div class="rule"></div>
  <p class="lede">Neque porro quisquam est qui dolorem ipsum quia dolor sit amet, consectetur, adipisci velit...</p>
  <div class="cards">
    <article class="card">
      <div class="card-media media-infra" role="img" aria-label="Hooded analyst facing screens with world maps in a dark control room"></div>
      <h3>Infrastructure<br>Penetration Testing</h3>
      <p>Sed ut perspiciatis unde omnis iste natus error sit voluptatem accusantium doloremque laudantium, totam rem aperiam, eaque ipsa quae ab illo inventore veritatis</p>
      <a class="read-more"><b>&gt;</b>Read More &gt;</a>
    </article>
    <article class="card featured">
      <div class="card-media media-app" role="img" aria-label="Colourful stack of data blocks on a glowing circuit board"></div>
      <h3>Application<br>Penetration Testing</h3>
      <p>Sed ut perspiciatis unde omnis iste natus error sit voluptatem accusantium doloremque laudantium, totam rem aperiam, eaque ipsa quae ab illo inventore veritatis</p>
      <a class="read-more"><b>&gt;</b>Read More &gt;</a>
    </article>
    <article class="card">
      <div class="card-media media-red" role="img" aria-label="Row of red-hooded figures at laptops under blue light"></div>
      <h3>Red Teaming</h3>
      <p>Sed ut perspiciatis unde omnis iste natus error sit voluptatem accusantium doloremque laudantium, totam rem aperiam, eaque ipsa quae ab illo inventore veritatis</p>
      <a class="read-more"><b>&gt;</b>Read More &gt;</a>
    </article>
  </div>
</section>

<section class="about">
  <div class="about-visual" role="img" aria-label="Consultant at a laptop in front of a large blue security shield and network lines"></div>
  <div class="about-copy">
    <h2 class="section-title">About <em>Vantage Keep</em></h2>
    <div class="rule"></div>
    <h4>Neque porro quisquam est qui dolorem ipsum quia dolor sit amet, consectetur, adipisci velit...</h4>
    <p>Sed ut perspiciatis unde omnis iste natus error sit voluptatem accusantium doloremque laudantium, totam rem aperiam, eaque ipsa quae ab illo inventore veritatis et quasi architecto beatae vitae dicta sunt explicabo.</p>
    <p>Nemo enim ipsam voluptatem quia voluptas sit aspernatur aut odit aut fugit, sed quia consequuntur magni dolores eos qui ratione voluptatem sequi nesciunt. Neque porro quisquam est, qui dolorem ipsum quia dolor sit amet, consectetur, adipisci velit, sed quia non numquam eius modi tempora incidunt ut labore et dolore magnam aliquam quaerat voluptatem.</p>
    <a class="btn-solid">LEARN MORE ABOUT US</a>
  </div>
</section>

<footer class="footer">
  <div class="brand"><span class="brand-mark"></span>VANTAGE KEEP</div>
  <div class="social" aria-label="Social links"><i></i><i></i><i></i><i></i><i></i></div>
  <div class="cols">
    <div class="col reach">
      <h5>To Reach Us</h5>
      <p><svg width="10" height="14" viewBox="0 0 10 14"><path fill="#0677BA" d="M5 0a5 5 0 0 0-5 5c0 4 5 9 5 9s5-5 5-9a5 5 0 0 0-5-5zm0 7a2 2 0 1 1 0-4 2 2 0 0 1 0 4z"/></svg>48 Marlow Street, Larkfield,<br>California, 93122.</p>
      <p><svg width="12" height="12" viewBox="0 0 24 24"><path fill="#0677BA" d="M6.6 10.8a15 15 0 0 0 6.6 6.6l2.2-2.2c.3-.3.7-.4 1-.2 1.1.4 2.3.6 3.6.6.6 0 1 .4 1 1V20c0 .6-.4 1-1 1A17 17 0 0 1 3 4c0-.6.4-1 1-1h3.5c.6 0 1 .4 1 1 0 1.3.2 2.5.6 3.6.1.3 0 .7-.2 1z"/></svg>0123 555 0142</p>
      <p><svg width="12" height="12" viewBox="0 0 12 12"><rect x="0.5" y="2" width="11" height="8" fill="none" stroke="#0677BA"/><path d="M.5 2l5.5 4 5.5-4" stroke="#0677BA" fill="none"/></svg>hello@vantagekeep.example</p>
    </div>
    <div class="col">
      <h5>Quick Links</h5>
      <ul>
        <li><i></i>Home</li><li><i></i>About Us</li><li><i></i>Services</li><li><i></i>Project</li><li><i></i>Industry News</li><li><i></i>Contact</li>
      </ul>
    </div>
    <div class="col subscribe">
      <h5>Subscribe</h5>
      <p>Neque porro quisquam est qui dolorem ipsum quia dolor sit amet,</p>
      <div class="subscribe-form"><span>Email Address</span><b><svg width="18" height="18" viewBox="0 0 24 24"><path fill="#fff" d="M2 11l20-9-7 20-3-8z"/></svg></b></div>
    </div>
  </div>
  <p class="copyright">Vantage Keep © 2024 All Rights Reserved.</p>
</footer>

</body>
</html>
```